Substance abuse awareness flyer for school age kids

I am needing a flyer for school-age kids. What if it were designed to look like an Voxtab with someone texting and the text bubbles were some of the text below with emojis? Maybe a text chain between to friends:

Maybe the first text bubble says "I'm thinking about using drugs and alcohol"
the next bubble: "Just say no!" ( perhaps a stop sign emoji ?)

"Talk to your parents, your teachers at school, or your doctor about how drugs and alcohol can harm you"

another text bubble "did you know that alcohol and drugs could lead to..."
then include some of the info below (see links for more info).
Where ever you get info, it must be cited.

this needs to be English on one side and Spanish on the other side and needs to include the logo attached.

The effects of substance abuse
BHW: https://www.bhwagency.org/youth/features/teen-substance-use.html
Affect growth and development, especially brain development. Not able to focus at school or be around friends. https://www.kestrowline.org/sites/default/files/preventingdruguse_2.pdf
Leads to risky behaviors and lack of impulse control (dangerous activities) https://www.kestrowline.org/sites/default/files/preventingdruguse_2.pdf
Contribute to health problems as an adult: heart disease, high blood pressure, and trouble sleeping.

Target Market(s)

school age kids 9-20

Requirements
Must have
• Print ready: 8.5x11

```html
<!DOCTYPE html>
<html lang="en">
<head>
<meta charset="utf-8">
<title>The Effects of Substance Abuse – Flyer</title>
<link rel="stylesheet" href="https://fonts.googleapis.com/css2?family=Bebas+Neue&family=Lato:wght@400;700;900&display=swap">
<style>
:root{
  --page-bg:#e6e6e8;
  --header-red:#c21f22;
  --header-maroon:#6e2233;
  --footer-maroon:#76293a;
  --footer-blue:#1b6fb6;
  --scene-light:#7f89a8;
  --scene-dark:#5b6688;
  --skin:#f0cdbc;
  --phone-white:#fbfbfc;
  --phone-edge:#d7d9de;
  --chat-blue:#5b86f0;
  --chat-bg:#e4e9fb;
  --bubble-white:#ffffff;
  --link-bg:#e9eaee;
  --text-dark:#3c3f47;
  --logo-blue:#1f5fa8;
  --white:#ffffff;
}
*{box-sizing:border-box;margin:0;padding:0}
html,body{width:1200px;height:1200px;overflow:hidden;background:var(--page-bg)}
body{position:relative;font-family:'Lato',sans-serif}

.flyer{position:absolute;left:193px;top:74px;width:813px;height:1053px;overflow:hidden;background:var(--scene-dark)}

.scene-art{position:absolute;left:0;top:100px;width:100%;height:880px;
  background:radial-gradient(ellipse at 30% 40%,var(--scene-light),var(--scene-dark) 75%)}
.hand-art{position:absolute;left:36px;top:340px;width:690px;height:640px;border-radius:260px 300px 60px 200px;
  background:linear-gradient(160deg,#f4d8ca,var(--skin));opacity:.95}

.header{position:absolute;left:0;top:0;width:100%;height:100px;
  background:linear-gradient(90deg,var(--header-red),#a81e2a 55%,var(--header-maroon))}
.header-title{position:absolute;left:221px;top:24px;font-family:'Bebas Neue',sans-serif;font-weight:400;font-size:52px;
  letter-spacing:0;color:var(--white);line-height:1;white-space:nowrap}
.header-rule{position:absolute;left:480px;top:73px;width:333px;height:3px;background:var(--white)}

.badge{position:absolute;left:19px;top:12px;width:176px;height:176px;border-radius:50%;
  background:var(--white);border:7px solid #a3202a;box-shadow:0 3px 8px rgba(0,0,0,.3);
  display:flex;align-items:center;justify-content:center;text-align:center}
.badge-name{font-family:'Lato',sans-serif;font-weight:900;font-size:19px;line-height:1.15;color:var(--logo-blue);letter-spacing:.5px}

.phone{position:absolute;left:219px;top:128px;width:395px;height:847px;border-radius:62px;
  background:var(--phone-white);border:2px solid var(--phone-edge);box-shadow:0 4px 14px rgba(0,0,0,.18)}
.phone-camera{position:absolute;left:410px;top:163px;width:14px;height:14px;border-radius:50%;background:#2a2c33}
.phone-sensor{position:absolute;left:355px;top:198px;width:9px;height:9px;border-radius:50%;background:#2a2c33}
.phone-speaker{position:absolute;left:383px;top:198px;width:66px;height:8px;border-radius:4px;background:#2a2c33}
.phone-home{position:absolute;left:389px;top:884px;width:54px;height:54px;border-radius:50%;border:2px solid var(--phone-edge);background:var(--phone-white)}

.chat{position:absolute;left:238px;top:222px;width:358px;height:665px;background:var(--chat-bg);border:1px solid var(--chat-blue)}
.chat-bar{position:absolute;left:0;top:0;width:100%;height:60px;background:var(--chat-blue)}
.chat-avatar{position:absolute;left:22px;top:5px;width:50px;height:50px;border-radius:50%;background:linear-gradient(#6b5142,#caa48e);border:2px solid var(--white)}
.chat-name{position:absolute;left:84px;top:18px;font-size:20px;color:var(--white)}
.chat-icons{position:absolute;right:14px;top:19px}

.bubble{position:absolute;font-size:14px;line-height:17.5px;color:var(--text-dark);border-radius:10px}
.bubble.sent{background:var(--chat-blue);color:var(--white);padding:6px 10px;white-space:nowrap;border-radius:14px}
.bubble.received{background:var(--bubble-white);padding:7px 14px;box-shadow:0 2px 3px rgba(0,0,0,.15)}
.bubble .link{display:block;background:var(--link-bg);margin:12px -4px 0 -6px;padding:2px 6px;font-size:13.5px;word-break:break-all}
.bubble p + p{margin-top:14px}

.footer-band{position:absolute;left:0;top:997px;width:100%;height:56px;background:var(--footer-maroon)}
.footer-url{position:absolute;left:0;top:994px;width:400px;height:59px;background:var(--footer-blue);border-radius:0 40px 0 0;
  display:flex;align-items:center;padding-left:34px;gap:10px;color:var(--white);font-weight:900;font-size:24px;white-space:nowrap}
.social{position:absolute;top:988px;width:40px;height:40px;border-radius:50%;background:var(--white);border:3px solid var(--footer-blue)}
.social.one{left:707px}.social.two{left:752px}
</style>
</head>
<body>
<div class="flyer">
  <div class="scene-art" role="img" aria-label="Blurred photo of pills and capsules scattered on a table"></div>
  <div class="hand-art" role="img" aria-label="A hand holding the phone"></div>

  <header class="header">
    <h1 class="header-title">The Effects of Substance Abuse</h1>
    <div class="header-rule"></div>
  </header>
  <div class="badge"><span class="badge-name">RIVERBEND<br>HEALTH<br>PARTNERS</span></div>

  <div class="phone"></div>
  <div class="phone-camera"></div>
  <div class="phone-sensor"></div>
  <div class="phone-speaker"></div>
  <div class="phone-home"></div>

  <section class="chat">
    <div class="chat-bar">
      <div class="chat-avatar" role="img" aria-label="Profile photo of the best friend"></div>
      <div class="chat-name">Best Friend</div>
      <svg class="chat-icons" width="84" height="22" viewBox="0 0 84 22">
        <rect x="0" y="4" width="20" height="14" rx="2" fill="#fff"/>
        <polygon points="20,11 30,4 30,18" fill="#fff"/>
        <path d="M44 3c2 0 3 4 2 5l-2 2c1 3 3 5 6 6l2-2c1-1 5 0 5 2l-1 3c-1 1-3 1-5 0-5-2-9-6-10-11 0-2 1-5 3-5z" fill="#fff"/>
        <circle cx="79" cy="3" r="2.2" fill="#fff"/><circle cx="79" cy="11" r="2.2" fill="#fff"/><circle cx="79" cy="19" r="2.2" fill="#fff"/>
      </svg>
    </div>

    <div class="bubble sent" style="left:32px;top:74px">Hey.. I'm thinking about using drugs or alcohol...</div>
    <div class="bubble received" style="left:15px;top:113px;width:247px;height:30px;padding-top:6px">Whattt?! NOOO!!!! &nbsp;🙅‍♀️👎❌</div>
    <div class="bubble received" style="left:13px;top:150px;width:300px">
      <p>Did you know that alcohol &amp; drugs could affect growth and development, especially brain development. Not able to focus at school or be around friends..</p>
      <span class="link">https://www.bhwagency.org/youth/features/teen-substance-use.html</span>
    </div>
    <div class="bubble sent" style="left:182px;top:293px">Sounds scary..... 😧</div>
    <div class="bubble received" style="left:13px;top:322px;width:300px">
      <p>YEA!! It also leads to risky behaviors &amp; lack of impulse control (dangerous activities)</p>
      <span class="link">https://www.kestrowline.org/sites/default/files/preventingdruguse_2.pdf</span>
      <p style="margin-top:14px">Also it Contribute to health problems as an adult: heart disease, high blood pressure, and trouble sleeping.</p>
      <span class="link">https://www.kestrowline.org/sites/default/files/preventingdruguse_2.pdf</span>
    </div>
    <div class="bubble received" style="left:13px;top:556px;width:300px">Talk to your parents, your teachers at school, or your doctor about how drugs &amp; alcohol can harm you"</div>
    <div class="bubble sent" style="left:157px;top:626px">I will.... Thanks, dear... ❤️</div>
  </section>

  <footer>
    <div class="footer-band"></div>
    <div class="footer-url">
      <svg width="24" height="24" viewBox="0 0 26 26" fill="none" stroke="#fff" stroke-width="2.2">
        <circle cx="13" cy="13" r="11"/><ellipse cx="13" cy="13" rx="5" ry="11"/><line x1="2" y1="13" x2="24" y2="13"/>
      </svg>
      <span>www.riverbend-health.org</span>
    </div>
    <div class="social one"></div>
    <div class="social two"></div>
  </footer>
</div>
</body>
</html>
```